Design an attractive wine label for Birch Vale Wines

we need a wine label design, we are an Australian wine exporting company'Birch Vale Wines'. We succeed several pallets in last few months and is going to launch our first container. So it’s time to start our own brands. we will have some wines display in China's shopping mall shelves, so we want to have a catchy label which can attract Chinese eyes immediately. other details you will see in the file i uploaded. The design should include a front and back label.

Target Market(s)

Birch Vale Wines are targeting middle class wine drinkers in 2nd-4th tier Chinese cities.

Colors

Designer to choose colors to be used in the design.

Requirements
Must have
• We’d like something that at first glance is Australian (element, style or color…) but subconsciously connects to the Chinese. Demeanor bearing in mind the demographics targeted across the ranges. We would expect the designs and naming to becoming more formalized as they rise to platinum.
Nice to have
• creative things come out
Should not have
• any dead related word or icon, no number '4' related word or icon, no skull related word or icon, kangaroo (see brand 'Crimson Wing')

```html
<!DOCTYPE html>
<html lang="en">
<head>
<meta charset="utf-8">
<title>Birch Vale Wines – Larrin &amp; Yarrowin labels</title>
<link rel="stylesheet" href="https://fonts.googleapis.com/css2?family=Great+Vibes&family=Cinzel:wght@400;500&display=swap">
<style>
  :root {
    --backdrop: #5d5b5c;
    --label-black: #121212;
    --label-black-soft: #1d1d1d;
    --gold: #c9b07a;
    --gold-light: #e8d9b0;
    --gold-dark: #8a7345;
    --wine-red: #a50d12;
    --wine-red-deep: #6e0508;
    --cream: #e6e1d6;
    --cream-dark: #cfc8b8;
    --ink: #1e1e1e;
    --accent-red: #c8102e;
    --white: #ffffff;
  }
  html, body {
    margin: 0;
    padding: 0;
    width: 1200px;
    height: 1200px;
    overflow: hidden;
    background: var(--backdrop);
  }
  .canvas {
    position: relative;
    width: 1200px;
    height: 1200px;
    display: flex;
    align-items: center;
    justify-content: center;
    gap: 80px;
  }
  .label {
    width: 460px;
    height: 580px;
    display: block;
    box-shadow: 0 18px 40px rgba(0,0,0,0.35);
  }
  .brand-name {
    font-family: 'Great Vibes', cursive;
    font-size: 76px;
    fill: var(--gold);
  }
  .varietal {
    font-family: 'Cinzel', serif;
    font-size: 25px;
    letter-spacing: 1px;
  }
  .vintage {
    font-family: 'Cinzel', serif;
    font-size: 19px;
    letter-spacing: 3px;
  }
  .region {
    font-family: 'Cinzel', serif;
    font-size: 11px;
    letter-spacing: 1px;
  }
  .region-script {
    font-family: 'Great Vibes', cursive;
    font-size: 32px;
    fill: var(--accent-red);
  }
  .on-red { fill: var(--white); }
  .on-cream { fill: var(--ink); }
</style>
</head>
<body>
<main class="canvas">

  <!-- Larrin · Merlot Cabernet -->
  <svg class="label label--larrin" viewBox="0 0 460 580" xmlns="http://www.w3.org/2000/svg">
    <defs>
      <linearGradient id="larrin-bg" x1="0" y1="0" x2="1" y2="1">
        <stop offset="0" stop-color="var(--label-black-soft)"/>
        <stop offset="1" stop-color="var(--label-black)"/>
      </linearGradient>
      <linearGradient id="larrin-red" x1="0" y1="0" x2="0" y2="1">
        <stop offset="0" stop-color="var(--wine-red)"/>
        <stop offset="1" stop-color="var(--wine-red-deep)"/>
      </linearGradient>
      <linearGradient id="larrin-gold" x1="0" y1="1" x2="1" y2="0">
        <stop offset="0" stop-color="var(--gold-dark)"/>
        <stop offset="0.5" stop-color="var(--gold-light)"/>
        <stop offset="1" stop-color="var(--gold)"/>
      </linearGradient>
      <linearGradient id="larrin-pattern" x1="0" y1="0" x2="1" y2="0">
        <stop offset="0" stop-color="#7a1a12"/>
        <stop offset="0.5" stop-color="#d9622b"/>
        <stop offset="1" stop-color="#e79a3a"/>
      </linearGradient>
      <linearGradient id="larrin-figures" x1="0" y1="0" x2="1" y2="0">
        <stop offset="0" stop-color="#8e2a1c" stop-opacity="0.55"/>
        <stop offset="1" stop-color="#d8782c" stop-opacity="0.8"/>
      </linearGradient>
    </defs>

    <rect class="label-ground" width="460" height="580" fill="url(#larrin-bg)"/>
    <text class="brand-name" x="230" y="105" text-anchor="middle">Larrin</text>

    <polygon class="figures-area" role="img" aria-label="Illustration of a procession of dancing figures in ochre tones"
             points="70,403 230,318 230,256 70,341" fill="url(#larrin-figures)"/>

    <polygon class="red-field" points="0,485 460,285 460,580 0,580" fill="url(#larrin-red)"/>
    <polygon class="dot-pattern" role="img" aria-label="Dot painting pattern band in ochre, orange and red"
             points="0,448 460,202 460,285 0,485" fill="url(#larrin-pattern)"/>
    <polygon class="gold-rule" points="0,440 460,194 460,204 0,450" fill="url(#larrin-gold)"/>

    <text class="varietal on-red" x="230" y="510" text-anchor="middle">Merlot Cabernet</text>
    <line x1="150" y1="536" x2="192" y2="536" stroke="var(--white)" stroke-width="1"/>
    <text class="vintage on-red" x="230" y="543" text-anchor="middle">2007</text>
    <line x1="268" y1="536" x2="310" y2="536" stroke="var(--white)" stroke-width="1"/>
    <text class="region on-red" x="230" y="566" text-anchor="middle">Western Australia</text>
  </svg>

  <!-- Yarrowin · Cabernet Sauvignon -->
  <svg class="label label--yarrowin" viewBox="0 0 460 580" xmlns="http://www.w3.org/2000/svg">
    <defs>
      <linearGradient id="yarrowin-bg" x1="0" y1="0" x2="1" y2="1">
        <stop offset="0" stop-color="var(--label-black-soft)"/>
        <stop offset="1" stop-color="var(--label-black)"/>
      </linearGradient>
      <linearGradient id="yarrowin-gold" x1="0" y1="0" x2="1" y2="0">
        <stop offset="0" stop-color="var(--gold-dark)"/>
        <stop offset="0.5" stop-color="var(--gold-light)"/>
        <stop offset="1" stop-color="var(--gold-dark)"/>
      </linearGradient>
      <linearGradient id="yarrowin-cream" x1="0" y1="0" x2="0" y2="1">
        <stop offset="0" stop-color="var(--cream)"/>
        <stop offset="1" stop-color="var(--cream-dark)"/>
      </linearGradient>
      <linearGradient id="yarrowin-figures" x1="0" y1="0" x2="0" y2="1">
        <stop offset="0" stop-color="var(--white)" stop-opacity="0.15"/>
        <stop offset="1" stop-color="var(--white)" stop-opacity="0.7"/>
      </linearGradient>
    </defs>

    <rect class="label-ground" width="460" height="580" fill="url(#yarrowin-bg)"/>
    <text class="brand-name" x="230" y="105" text-anchor="middle">Yarrowin</text>

    <rect class="figures-area" role="img" aria-label="White silhouettes of a group of dancers"
          x="150" y="310" width="160" height="70" rx="3" fill="url(#yarrowin-figures)"/>

    <rect class="gold-band" x="0" y="384" width="460" height="18" fill="url(#yarrowin-gold)"/>
    <rect class="cream-band" x="0" y="402" width="460" height="178" fill="url(#yarrowin-cream)"/>

    <text class="varietal on-cream" x="230" y="474" text-anchor="middle">Cabernet Sauvignon</text>
    <line x1="140" y1="502" x2="190" y2="502" stroke="var(--ink)" stroke-width="1"/>
    <text class="vintage on-cream" x="230" y="509" text-anchor="middle">2008</text>
    <line x1="270" y1="502" x2="320" y2="502" stroke="var(--ink)" stroke-width="1"/>
    <text class="region-script" x="230" y="548" text-anchor="middle">Australia</text>
  </svg>

</main>
</body>
</html>
```